Tallow Crest Business Card

We need a business card designed for a a company called "Tallow Crest". We offer consulting, coaching and training to business leaders and coaches (across the world) using the latest findings in neuroscience, social and emotional intelligence and positive psychology. The final design should communicate the use of brain science to create sustainable relationships.

The card should be doublesided. The logo is attached and names and titles will be provided to the successful designer. Thank you.

Industry/Entity Type

Training

```html
<!DOCTYPE html>
<html lang="en">
<head>
<meta charset="utf-8">
<title>Tallow Crest Business Card</title>
<link rel="stylesheet" href="https://fonts.googleapis.com/css2?family=Montserrat:wght@800&family=Raleway:wght@300;400&display=swap">
<style>
  :root {
    --page-bg: #ffffff;
    --card-front-bg: #f1f1f1;
    --brand-blue: #1b8fb4;
    --brand-green: #b3cf2c;
    --gradient-start: #0d8fb3;
    --gradient-mid: #1fa0ac;
    --gradient-end: #bcd631;
    --divider: #6d6d6d;
    --mark-faint: rgba(255, 255, 255, 0.45);
    --brain-tone: #7fae95;
  }
  * { margin: 0; padding: 0; box-sizing: border-box; }
  html, body {
    width: 1200px;
    height: 810px;
    overflow: hidden;
    background: var(--page-bg);
  }
  .sheet {
    position: relative;
    width: 1200px;
    height: 810px;
  }
  .card {
    position: absolute;
    top: 270px;
    width: 500px;
    height: 256px;
  }
  .card--front {
    left: 80px;
    background: var(--card-front-bg);
    text-align: center;
  }
  .card--back {
    left: 676px;
    background: linear-gradient(90deg, var(--gradient-start) 0%, var(--gradient-mid) 40%, var(--gradient-end) 100%);
    text-align: center;
  }
  .divider {
    position: absolute;
    left: 618px;
    top: 282px;
    width: 1px;
    height: 236px;
    background: var(--divider);
  }
  .brand {
    display: inline-flex;
    align-items: center;
    gap: 12px;
  }
  .brand__dot {
    width: 26px;
    height: 26px;
    border-radius: 50%;
    background: var(--brand-green);
  }
  .brand__name {
    font-family: "Montserrat", sans-serif;
    font-weight: 800;
    color: var(--brand-blue);
    font-size: 40px;
    letter-spacing: 1px;
    text-transform: uppercase;
  }
  .card--front .brand { margin-top: 74px; }
  .tagline {
    margin-top: 36px;
    display: flex;
    justify-content: center;
    align-items: center;
    gap: 8px;
    font-family: "Raleway", sans-serif;
    font-weight: 400;
    font-size: 18px;
    text-transform: uppercase;
  }
  .tagline__love { color: var(--brand-blue); }
  .tagline__friendship { color: var(--brand-green); }
  .tagline__arrow { display: block; }
  .tagline__brain {
    width: 70px;
    height: 44px;
    border-radius: 50%;
    background: radial-gradient(ellipse at center, var(--brain-tone) 0%, var(--brand-blue) 100%);
  }
  .contact-heading {
    margin-top: 34px;
    font-family: "Raleway", sans-serif;
    font-weight: 300;
    font-size: 24px;
    color: #ffffff;
    letter-spacing: 1px;
    text-transform: uppercase;
  }
  .card--back .brand { margin-top: 66px; }
  .card--back .brand__name { color: var(--mark-faint); font-size: 30px; }
  .card--back .brand__dot { background: var(--mark-faint); width: 20px; height: 20px; }
</style>
</head>
<body>
<main class="sheet">
  <section class="card card--front" aria-label="Card front">
    <div class="brand">
      <span class="brand__dot"></span>
      <span class="brand__name">Tallow Crest</span>
    </div>
    <div class="tagline">
      <span class="tagline__love">Love</span>
      <svg class="tagline__arrow" width="28" height="10" viewBox="0 0 28 10" aria-hidden="true">
        <path d="M0 5 H25 M20 1 L26 5 L20 9" fill="none" stroke="#1b8fb4" stroke-width="1.4"/>
      </svg>
      <div class="tagline__brain" role="img" aria-label="Illustration of a human brain"></div>
      <svg class="tagline__arrow" width="28" height="10" viewBox="0 0 28 10" aria-hidden="true">
        <path d="M0 5 H25 M20 1 L26 5 L20 9" fill="none" stroke="#b3cf2c" stroke-width="1.4"/>
      </svg>
      <span class="tagline__friendship">Friendship</span>
    </div>
  </section>

  <div class="divider" aria-hidden="true"></div>

  <section class="card card--back" aria-label="Card back">
    <h2 class="contact-heading">Contact Information</h2>
    <div class="brand">
      <span class="brand__dot"></span>
      <span class="brand__name">Tallow Crest</span>
    </div>
  </section>
</main>
</body>
</html>
```